Torvane Systems*

Stationary design including business cards, letter heads, envelops and email signatures using our new logo

Target Market(s)

Innovative Technologies

Industry/Entity Type

Defense Contracting

Font styles to use
Sans Serif

```html
<!DOCTYPE html>
<html lang="en">
<head>
<meta charset="utf-8">
<title>Torvane Systems — Stationery</title>
<link href="https://fonts.googleapis.com/css2?family=Work+Sans:wght@400;500;600&display=swap" rel="stylesheet">
<style>
:root{
  --backdrop:#b4b4b4;
  --paper:#ffffff;
  --ink:#111111;
  --flap:#f2f2f2;
  --rule:#555555;
  --panel:#0f0f0f;
  --shadow:rgba(0,0,0,.45);
}
*{margin:0;padding:0;box-sizing:border-box}
html,body{width:1200px;height:1044px;overflow:hidden}
body{background:var(--backdrop);font-family:"Work Sans",Arial,sans-serif;color:var(--ink);position:relative}
.sheet{position:absolute;background:var(--paper);box-shadow:2px 2px 2px var(--shadow);overflow:hidden}
.brand{display:flex;align-items:center;gap:4px;font-family:"Work Sans",Arial,sans-serif;font-weight:600;color:var(--ink);white-space:nowrap;letter-spacing:.02em}
.brand .mark{display:inline-block;background:var(--ink)}
.icon{width:1em;height:1em;vertical-align:-.12em;margin-right:.25em}
.contact-list{list-style:none;line-height:1.35}
.address{text-align:right;line-height:1.35}

/* letterhead */
.letterhead{left:166px;top:119px;width:406px;height:573px}
.letterhead .brand{position:absolute;top:74px;left:0;right:0;justify-content:center;font-size:11px}
.letterhead .brand .mark{width:7px;height:7px}
.letterhead .rule{position:absolute;left:39px;right:39px;top:515px;border-top:1px solid var(--rule)}
.letterhead .contact-list{position:absolute;left:39px;top:533px;font-size:6.6px}
.letterhead .address{position:absolute;right:39px;top:541px;font-size:6.6px}

/* business cards */
.card{top:119px;width:205px;height:117px}
.card-front{left:613px}
.card-back{left:829px}
.card-front .brand{position:absolute;right:13px;top:43px;font-size:8px}
.card-front .brand .mark{width:5px;height:5px}
.card-front .holder{position:absolute;left:13px;top:62px}
.card-front .holder-name{font-size:7px;font-weight:600;letter-spacing:.06em}
.card-front .holder-role{font-size:5px}
.card-front .rule{position:absolute;left:13px;right:13px;top:81px;border-top:1px solid var(--rule)}
.card-front .contact-list{position:absolute;left:13px;top:87px;font-size:5.3px}
.card-front .address{position:absolute;right:13px;top:94px;font-size:5.3px}
.card-back .brand{position:absolute;left:0;right:0;top:50px;justify-content:center;font-size:11px}
.card-back .brand .mark{width:7px;height:7px}

/* envelopes */
.envelope{left:613px;width:421px;height:197px}
.envelope-back{top:266px}
.envelope-back .flap{position:absolute;left:0;top:0;width:421px;height:64px}
.envelope-back .brand{position:absolute;left:0;right:0;top:19px;justify-content:center;font-size:18px}
.envelope-back .brand .mark{width:10px;height:10px}
.envelope-front{top:495px}
.envelope-front .brand{position:absolute;left:19px;top:54px;font-size:8.5px}
.envelope-front .brand .mark{width:5px;height:5px}
.envelope-front .address{position:absolute;left:19px;top:168px;text-align:left;font-size:7px}

/* email signature */
.signature{left:166px;top:724px;width:866px;height:200px;display:flex}
.signature .brand-panel{width:211px;height:100%;background:var(--panel);display:flex;align-items:center;justify-content:center}
.signature .brand-panel .brand{color:#fff;font-size:22px;font-weight:500}
.signature .brand-panel .brand .mark{width:12px;height:12px;background:#fff}
.signature .details{padding:24px 0 0 36px;font-size:12px;letter-spacing:.02em}
.signature .holder-name{font-size:15px;font-weight:500;letter-spacing:.08em;line-height:1.1}
.signature .holder-role{font-size:12px;margin-top:1px}
.signature .social{display:flex;gap:8px;margin:14px 0 13px}
.signature .social span{width:19px;height:19px;border-radius:3px;background:var(--ink);display:block}
.signature .address{text-align:left;line-height:1.25}
.signature .contact-list{margin-top:7px;line-height:1.2}
</style>
</head>
<body>

<svg width="0" height="0" style="position:absolute" aria-hidden="true">
  <symbol id="i-phone" viewBox="0 0 16 16"><path d="M4 1.5l2.2 3-1.3 1.6c.8 1.8 2.2 3.3 4 4.2l1.6-1.3 3 2.2-1.2 2.7C7 13.8 2.2 9 1.3 2.7z" fill="currentColor"/></symbol>
  <symbol id="i-mail" viewBox="0 0 16 16"><rect x="1.5" y="3.5" width="13" height="9" fill="none" stroke="currentColor" stroke-width="1.5"/><path d="M1.5 4l6.5 5 6.5-5" fill="none" stroke="currentColor" stroke-width="1.5"/></symbol>
  <symbol id="i-globe" viewBox="0 0 16 16"><g fill="none" stroke="currentColor" stroke-width="1.3"><circle cx="8" cy="8" r="6.3"/><ellipse cx="8" cy="8" rx="2.8" ry="6.3"/><path d="M1.7 8h12.6"/></g></symbol>
</svg>

<section class="sheet letterhead" aria-label="Letterhead">
  <div class="brand"><span class="mark"></span>Torvane Systems</div>
  <div class="rule"></div>
  <ul class="contact-list">
    <li><svg class="icon"><use href="#i-phone"/></svg>555 014 2290</li>
    <li><svg class="icon"><use href="#i-mail"/></svg>info@torvanesystems.com</li>
    <li><svg class="icon"><use href="#i-globe"/></svg>www.torvanesystems.com</li>
  </ul>
  <p class="address">418 Alder Street<br>Brookfield, WA 99021</p>
</section>

<section class="sheet card card-front" aria-label="Business card front">
  <div class="brand"><span class="mark"></span>Torvane Systems</div>
  <div class="holder">
    <p class="holder-name">DANIEL HART</p>
    <p class="holder-role">Founder</p>
  </div>
  <div class="rule"></div>
  <ul class="contact-list">
    <li><svg class="icon"><use href="#i-phone"/></svg>555 014 2290</li>
    <li><svg class="icon"><use href="#i-mail"/></svg>info@torvanesystems.com</li>
    <li><svg class="icon"><use href="#i-globe"/></svg>www.torvanesystems.com</li>
  </ul>
  <p class="address">418 Alder Street<br>Brookfield, WA 99021</p>
</section>

<section class="sheet card card-back" aria-label="Business card back">
  <div class="brand"><span class="mark"></span>Torvane Systems</div>
</section>

<section class="sheet envelope envelope-back" aria-label="Envelope back">
  <svg class="flap" viewBox="0 0 421 64" aria-hidden="true">
    <path d="M0 0H421L406 56Q404 63 396 63H26Q18 63 16 56Z" fill="var(--flap)"/>
  </svg>
  <div class="brand"><span class="mark"></span>Torvane Systems</div>
</section>

<section class="sheet envelope envelope-front" aria-label="Envelope front">
  <div class="brand"><span class="mark"></span>Torvane Systems</div>
  <p class="address">418 Alder Street<br>Brookfield, WA 99021</p>
</section>

<section class="sheet signature" aria-label="Email signature">
  <div class="brand-panel">
    <div class="brand"><span class="mark"></span>Torvane Systems</div>
  </div>
  <div class="details">
    <p class="holder-name">DANIEL HART</p>
    <p class="holder-role">Founder</p>
    <div class="social"><span aria-label="Professional network profile"></span><span aria-label="Social profile"></span></div>
    <p class="address">418 Alder Street<br>Brookfield, WA 99021</p>
    <ul class="contact-list">
      <li><svg class="icon"><use href="#i-phone"/></svg>555 014 2290</li>
      <li><svg class="icon"><use href="#i-mail"/></svg>info@torvanesystems.com</li>
      <li><svg class="icon"><use href="#i-globe"/></svg>www.torvanesystems.com</li>
    </ul>
  </div>
</section>

</body>
</html>
```